Kestrel Calisthenics Gym Website

We need a website design for our gym.

Kestrel is the UAE's first calisthenics and parkour gym. The theme under which the gym revolves is that one does not require any machinery to workout as our bodies could be themselves the machinery. The gym is designed to be the more of a social hub rather than an "in-and-out" gym, where people come train, have fun, hang out and socialize for a few hours rather than just train for 60 minutes then leave. The gym is designed to be a big open space with lots of natural sunlight, natural wood and plants all over the place to create a natural and refreshing setting. We also use recycled material throughout the gym and recycle our waste as being green is part of our philosophy. We currently also have some of the world's top and most recognized calisthenics athletes working with us.

We would like our website to reflect all that as well as provide a simple, interactive and fun way for visitors to be able to get class and gym information, check out gym media and contact us for bookings.

Target Market(s)

Ages 15-35

Industry/Entity Type

Fitness

Coding

Coded - Design and coding required

Number of Pages Required

4 page

Font styles to use
Decorative

Colors
0792cd

Requirements
Must have
• Class descriptions
• Gym description
• Class schedules
• Trainer profiles
• Gym philosophy
• Contact Details
Nice to have
• A link to contact us directly for a free first trial class

```html
<!DOCTYPE html>
<html lang="en">
<head>
<meta charset="utf-8">
<title>Kestrel Calisthenics Gym</title>
<link href="https://fonts.googleapis.com/css2?family=Open+Sans:ital,wght@0,400;0,600;0,700;1,400;1,600;1,700&family=Open+Sans+Condensed:wght@300&display=swap" rel="stylesheet">
<style>
:root{
  --blue:#0792cd;
  --sky:#00b4ec;
  --deep:#0678b0;
  --pale:#a9ddf5;
  --page:#f0f0f0;
  --ink:#444;
  --muted:#666;
  --grey:#d3d3d3;
  --red:#e0483e;
  --white:#fff;
}
*{box-sizing:border-box;margin:0;padding:0}
html,body{width:1200px;height:2899px;overflow:hidden}
body{position:relative;background:var(--page);font-family:"Open Sans",Arial,sans-serif;color:var(--ink)}
.abs{position:absolute}
a{color:inherit;text-decoration:none}

/* header */
.topbar{left:0;top:0;width:1200px;height:39px;background:var(--sky)}
.navbar{left:0;top:39px;width:1200px;height:96px;background:var(--blue)}
.logo{left:0;top:0;width:361px;height:135px;background:var(--white);display:flex;align-items:center;justify-content:center;gap:14px}
.logo-dot{width:22px;height:22px;border-radius:50%;background:var(--blue)}
.logo-name{font-weight:700;font-size:38px;color:#222;letter-spacing:-.5px}
.contact-top{left:384px;top:10px;font-size:13px;color:var(--white);display:flex;gap:34px}
.contact-top span{display:flex;align-items:center;gap:8px}
.social-top{left:1028px;top:12px;display:flex;gap:14px}
.social-top i,.social-bottom i{display:block;width:12px;height:12px;border-radius:50%;background:var(--white)}
.menu{left:557px;top:77px;display:flex;gap:0;font-size:13px;color:var(--white);font-weight:600}
.menu a{padding:10px 19px;text-transform:uppercase}
.menu a.current{background:var(--white);color:var(--blue)}

/* hero */
.hero{left:0;top:135px;width:1200px;height:443px;background:linear-gradient(100deg,#3a3532 0%,#6b5f55 30%,#8a8d8c 55%,#4d5a3f 75%,#7b8a55 100%)}
.hero-box{left:93px;top:236px;width:487px;height:228px;background:rgba(7,146,205,.82);border:2px solid rgba(255,255,255,.35);padding:22px 20px;color:var(--white)}
.hero-box h1{font-size:22px;line-height:28px;font-weight:700;text-transform:uppercase}
.hero-box p{font-size:12.5px;line-height:18px;margin-top:10px}
.hero-btn{display:block;width:234px;margin:20px auto 0;border:1px solid var(--white);text-align:center;font-size:14px;font-weight:600;padding:8px 0;text-transform:uppercase}

/* about */
.about-img{left:127px;top:609px;width:379px;height:257px;border-radius:6px;background:linear-gradient(180deg,#8a5a36 0%,#6f8a3e 45%,#4e3a2a 75%,#2b2b2b 100%)}
.about-title{left:568px;top:656px;font-size:30px;font-weight:600;color:#555}
.about-text{left:568px;top:700px;width:540px;font-size:12.5px;line-height:24px;color:var(--muted)}

/* live cards */
.live{width:321px;height:223px;background:var(--blue)}
.live-head{height:50px;display:flex;justify-content:space-between;align-items:center;padding:0 12px;color:var(--white);font-size:17px;font-style:italic}
.live-head b{font-weight:700}
.live-head small{font-style:normal;font-weight:700;font-size:12px}
.live-photo{height:167px}
.live-bar{height:6px;background:var(--sky)}

/* section headings */
.sec-title{font-size:20px;color:var(--blue);text-transform:uppercase;text-align:center;font-weight:400}

/* classes */
.classes{left:93px;top:1233px;width:668px;height:228px;background:var(--blue);padding:14px 14px;display:flex;gap:14px;color:var(--white)}
.class-col{flex:1;display:flex;flex-direction:column}
.class-col+.class-col{border-left:1px solid rgba(255,255,255,.5);padding-left:14px}
.class-row{height:50px;display:flex;align-items:center;justify-content:space-between;border-bottom:1px solid rgba(255,255,255,.6);font-size:13px;text-transform:uppercase}
.class-row span{display:flex;align-items:center;gap:8px}
.class-icons{display:flex;gap:16px}
.membership{left:786px;top:1233px;width:321px;height:228px;background:var(--sky);color:var(--white);text-align:center;padding-top:38px}
.membership h3{font-size:16px;font-weight:700}
.membership p{font-size:13.5px;line-height:21px;margin-top:10px}
.more-btn{display:inline-block;margin-top:20px;border:1px solid var(--white);padding:5px 26px;font-size:14px}

/* trainers, events, blog */
.panel{top:1565px;width:321px;height:276px}
.trainers{left:93px;background:var(--white);overflow:hidden}
.trainer{position:absolute;top:26px;width:150px;text-align:center}
.trainer-photo{width:88px;height:88px;border-radius:50%;margin:0 auto;background:radial-gradient(circle,#d9b9a3,#8c4a3a 70%,#5a3b35)}
.trainer h4{font-size:14px;color:var(--sky);font-weight:400;margin-top:40px}
.trainer em{display:block;font-size:13px;color:var(--sky)}
.trainer p{font-size:11.5px;font-style:italic;color:#555;margin-top:6px;line-height:15px}
.events{left:440px;background:var(--pale)}
.event{position:absolute;left:15px;width:295px;height:120px}
.event-photo{position:absolute;left:0;top:24px;width:99px;height:69px;background:linear-gradient(135deg,#d7d7d7,#6c6c6c)}
.event-date{position:absolute;left:0;top:0;font-size:11px;font-weight:700;color:var(--white)}
.event-time{position:absolute;left:160px;top:0;font-size:11px;font-weight:700;color:var(--red)}
.event-body{position:absolute;left:140px;top:20px;width:140px;text-align:center}
.event-body h5{font-size:17px;font-weight:400;color:#333}
.event-body p{font-size:11.5px;line-height:17px;color:#444;margin-top:4px}
.reserve{display:inline-block;margin-top:6px;border:1px solid var(--red);color:var(--red);font-size:11px;padding:1px 8px;background:var(--white)}
.blog{left:786px;background:var(--grey)}
.post{position:absolute;left:18px;width:290px;height:70px}
.post-photo{position:absolute;left:0;top:0;width:70px;height:62px;border:3px solid var(--white);background:linear-gradient(135deg,#e8cfbf,#9a6f5a)}
.post p{position:absolute;left:84px;top:0;font-size:11px;line-height:17px;color:var(--white)}
.post time{position:absolute;left:84px;top:40px;font-size:11px;color:#555}

/* gallery + hours */
.gallery{left:93px;top:2002px;width:668px;height:359px;display:grid;grid-template-columns:270px 275px 111px;grid-template-rows:177px 177px;gap:5px}
.gallery div:nth-child(1){background:linear-gradient(135deg,#c9a88f,#5d6b78)}
.gallery div:nth-child(2){background:linear-gradient(135deg,#e8e0d8,#a88a70)}
.gallery div:nth-child(3){background:linear-gradient(135deg,#bca393,#3e3e3e)}
.gallery div:nth-child(4){background:linear-gradient(135deg,#8c7466,#2c2c2c)}
.gallery div:nth-child(5){background:linear-gradient(135deg,#d3c1b4,#5b5b5b)}
.gallery div:nth-child(6){background:linear-gradient(135deg,#d5d5d5,#3a3a3a)}
.hours{left:786px;top:2002px;width:348px;height:363px;background:var(--blue);color:var(--white);padding:0 12px}
.hours h3{font-family:"Open Sans Condensed","Open Sans",sans-serif;font-weight:300;font-size:30px;text-align:center;padding:10px 0 8px;border-bottom:1px solid rgba(255,255,255,.6)}
.hours h3 b{font-weight:400}
.hour-row{height:28px;display:flex;justify-content:space-between;align-items:center;border-bottom:1px solid rgba(255,255,255,.5);font-size:11.5px}
.hour-row span{display:flex;align-items:center;gap:8px}
.hours p{font-size:11.5px;line-height:17px;text-align:center;margin-top:18px}
.hours strong{display:block;text-align:center;font-style:italic;font-weight:600;font-size:22px;margin-top:18px}

/* tweet */
.tweet-mark{left:243px;top:2462px;width:62px;height:62px;border-radius:50%;background:var(--sky)}
.tweet{left:347px;top:2472px;width:590px;font-size:12px;line-height:20px;color:var(--sky)}
.tweet span{color:#555}

/* footer */
.footer{left:0;top:2610px;width:1200px;height:246px;background:var(--blue);color:var(--white)}
.foot-bar{left:0;top:2856px;width:1200px;height:43px;background:var(--sky);color:var(--white);font-size:12px}
.f-title{font-size:16px;text-transform:uppercase}
.newsletter{left:93px;top:2650px;width:290px}
.newsletter p{font-size:12px;line-height:18px;margin-top:14px;text-transform:uppercase}
.field{width:285px;height:34px;background:var(--pale);margin-top:16px;font-size:11.5px;color:var(--white);padding:9px 16px}
.submit{width:207px;height:34px;background:var(--red);margin-top:8px;font-size:11.5px;padding:9px 12px;display:flex;justify-content:space-between}
.foot-about{left:441px;top:2643px;width:305px;font-size:12px;line-height:20px}
.foot-contact{left:441px;top:2740px;font-size:12px;line-height:40px}
.foot-contact b{font-style:italic;font-size:15px;margin-left:14px}
.foot-list{top:2650px}
.foot-list ul{list-style:none;margin-top:12px;font-size:12px;line-height:22px}
.foot-list li:before{content:"›";margin-right:10px}
.social-bottom{left:936px;top:2873px;display:flex;gap:16px}
</style>
</head>
<body>

<header>
  <div class="abs topbar"></div>
  <div class="abs navbar"></div>
  <div class="abs logo"><span class="logo-dot"></span><span class="logo-name">kestrel.</span></div>
  <div class="abs contact-top">
    <span><svg width="12" height="12" viewBox="0 0 12 12"><path d="M2 1l2 0 1 3-1.5 1a7 7 0 0 0 3.5 3.5L8 7l3 1v2a1 1 0 0 1-1 1A9 9 0 0 1 1 2a1 1 0 0 1 1-1z" fill="#fff"/></svg>1-200-555-0148</span>
    <span><svg width="13" height="10" viewBox="0 0 13 10"><rect x=".5" y=".5" width="12" height="9" fill="none" stroke="#fff"/><path d="M.5 .5l6 5 6-5" fill="none" stroke="#fff"/></svg>hello@kestrelgym.example</span>
  </div>
  <div class="abs social-top"><i></i><i></i><i></i><i></i></div>
  <nav class="abs menu">
    <a class="current" href="#">Home</a><a href="#">About</a><a href="#">Trainers</a><a href="#">Classes</a><a href="#">Blog</a><a href="#">Pricing</a><a href="#">Contact</a>
  </nav>
</header>

<section>
  <div class="abs hero" role="img" aria-label="Athlete doing pull-ups on a bar in an open gym with plants and clothing rack"></div>
  <div class="abs hero-box">
    <h1>Lorem ipsum dolor sit amet,<br>consec teteur adipiscing elit</h1>
    <p>Lorem ipsum dolor sit amet, consectetuer adipiscing elit, sed diam nonummy nibh euismod tincidunt ut laoreet dolore magna. Lorem ipsum dolor sit amet, consectetuer adipiscing elit, sed diam nonummy nibh euismod tincidunt ut laoreet dolore magna.</p>
    <a class="hero-btn" href="#">Contact for free class</a>
  </div>
</section>

<section>
  <div class="abs about-img" role="img" aria-label="Gym name in green plant lettering on a wooden wall above dumbbell rack"></div>
  <h2 class="abs about-title">Kestrel Calisthenics Gym</h2>
  <p class="abs about-text">Lorem ipsum dolor sit amet, aliquam erat volutpat. Ut wisi enim ad minim veniam, quis nostrud exerci tation ullamcorper suscipit lobortis nisl ut aliquip ex ea commodo consequat. Lorem ipsum dolor sit amet, aliquam erat volutpat. Ut wisi enim ad minim veniam, quis nostrud exerci tation ullamcorper suscipit lobortis nisl ut aliquip ex ea commodo consequat.</p>
</section>

<section>
  <div class="abs live" style="left:93px;top:896px">
    <div class="live-head"><span><b>LIVE</b> SPINNING</span><small>ROOM 2</small></div>
    <div class="live-photo" role="img" aria-label="Spinning class riding stationary bikes" style="background:linear-gradient(135deg,#d8b8a6,#c44a7a 50%,#333)"></div>
    <div class="live-bar"></div>
  </div>
  <div class="abs live" style="left:440px;top:896px">
    <div class="live-head"><span><b>LIVE</b> GYM</span><small>ROOM 1</small></div>
    <div class="live-photo" role="img" aria-label="Members training on elliptical machines" style="background:linear-gradient(135deg,#b07a4e,#e8d8c8 50%,#7a6a9a)"></div>
    <div class="live-bar"></div>
  </div>
  <div class="abs live" style="left:786px;top:896px">
    <div class="live-head"><span><b>LIVE</b> PILATES</span><small>ROOM 4</small></div>
    <div class="live-photo" role="img" aria-label="Pilates class seated with exercise balls" style="background:linear-gradient(135deg,#e6e6ec,#7a8ab8 60%,#3a4a8a)"></div>
    <div class="live-bar"></div>
  </div>
</section>

<section>
  <h2 class="abs sec-title" style="left:93px;top:1188px;width:668px">All classes</h2>
  <h2 class="abs sec-title" style="left:786px;top:1188px;width:321px">Membership prices</h2>
  <div class="abs classes">
    <div class="class-col">
      <div class="class-row"><span>◴ Cardio fitness</span><span class="class-icons">▦ ✉ ♡ ➦</span></div>
      <div class="class-row"><span>◴ Spinning</span><span class="class-icons">▦ ✉ ♡ ➦</span></div>
      <div class="class-row"><span>◴ Pilates</span><span class="class-icons">▦ ✉ ♡ ➦</span></div>
      <div class="class-row"><span>◴ Boxing</span><span class="class-icons">▦ ✉ ♡ ➦</span></div>
    </div>
    <div class="class-col">
      <div class="class-row"><span>◴ Aerobics</span><span class="class-icons">▦ ✉ ♡ ➦</span></div>
      <div class="class-row"><span>◴ Kik boxing</span><span class="class-icons">▦ ✉ ♡ ➦</span></div>
      <div class="class-row"><span>◴ Crossfit</span><span class="class-icons">▦ ✉ ♡ ➦</span></div>
      <div class="class-row"><span>◴ Yoga</span><span class="class-icons">▦ ✉ ♡ ➦</span></div>
    </div>
  </div>
  <div class="abs membership">
    <h3>25% DISCOUNT OF FOR ALL MEMBERS</h3>
    <p>Discount on services and<br>treatments at the Kestrel Club for<br>all membership cards holders.</p>
    <a class="more-btn" href="#">More</a>
  </div>
</section>

<section>
  <h2 class="abs sec-title" style="left:93px;top:1531px;width:321px">Our trainers</h2>
  <h2 class="abs sec-title" style="left:440px;top:1531px;width:321px">Next events</h2>
  <h2 class="abs sec-title" style="left:786px;top:1531px;width:321px">From the blog</h2>

  <div class="abs panel trainers">
    <div class="trainer" style="left:55px"><div class="trainer-photo" role="img" aria-label="Trainer portrait"></div><h4>LOREM IPSUM</h4><em>KIK BOXING</em><p>Lorem ipsum dolor<br>sit amet, consectetuer.</p></div>
    <div class="trainer" style="left:195px"><div class="trainer-photo" role="img" aria-label="Trainer portrait"></div><h4>LOREM IPSUM</h4><em>SPINNING</em><p>Lorem ipsum dolor<br>sit amet, consectetuer.</p></div>
    <svg class="abs" style="left:4px;top:120px" width="14" height="24"><path d="M12 2L3 12l9 10" fill="none" stroke="#00b4ec" stroke-width="2"/></svg>
    <svg class="abs" style="left:300px;top:120px" width="14" height="24"><path d="M2 2l9 10-9 10" fill="none" stroke="#00b4ec" stroke-width="2"/></svg>
  </div>

  <div class="abs panel events">
    <div class="event" style="top:22px"><span class="event-date">26 APRIL, 2014</span><span class="event-time">h.12.00-h.13.00</span><div class="event-photo" role="img" aria-label="Aerobics class"></div><div class="event-body"><h5>AEROBICS</h5><p>Lorem ipsum dolor sit amet, consectetuer adipiscing elit..</p><span class="reserve">RESERVATION</span></div></div>
    <div class="event" style="top:168px"><span class="event-date">26 APRIL, 2014</span><span class="event-time">h.12.00-h.13.00</span><div class="event-photo" role="img" aria-label="Spinning class"></div><div class="event-body"><h5>SPINNING</h5><p>Lorem ipsum dolor sit amet.</p><span class="reserve">RESERVATION</span></div></div>
  </div>

  <div class="abs panel blog">
    <div class="post" style="top:18px"><div class="post-photo" role="img" aria-label="Blog thumbnail"></div><p>nostrud exerci tation ullamcorper<br>suscipit lobortis nisl ut aliquip</p><time>25 April, 2014</time></div>
    <div class="post" style="top:102px"><div class="post-photo" role="img" aria-label="Blog thumbnail"></div><p>soluta nobis eleifend option congue<br>nihil imperdiet doming id</p><time>25 April, 2014</time></div>
    <div class="post" style="top:186px"><div class="post-photo" role="img" aria-label="Blog thumbnail"></div><p>quod mazim placerat facer possim<br>assum. Typi non habent</p><time>25 April, 2014</time></div>
  </div>
</section>

<section>
  <h2 class="abs sec-title" style="left:93px;top:1951px;width:668px">Gallery</h2>
  <div class="abs gallery">
    <div role="img" aria-label="Women in a group fitness class"></div>
    <div role="img" aria-label="Aerobics class on a wooden floor"></div>
    <div role="img" aria-label="Member stretching"></div>
    <div role="img" aria-label="Woman lifting dumbbells"></div>
    <div role="img" aria-label="Woman on a bench press"></div>
    <div role="img" aria-label="Dumbbells on a rack"></div>
  </div>
  <div class="abs hours">
    <h3>Opening <b>Hours</b></h3>
    <div class="hour-row"><span>▦ Monday</span>h.6:00-h.24:00</div>
    <div class="hour-row"><span>▦ Tuesday</span>h.6:00-h.24:00</div>
    <div class="hour-row"><span>▦ Wednesday</span>h.6:00-h.24:00</div>
    <div class="hour-row"><span>▦ Thursday</span>h.6:00-h.24:00</div>
    <div class="hour-row"><span>▦ Friday</span>h.6:00-h.24:00</div>
    <div class="hour-row"><span>▦ Saturday</span>h.6:00-h.24:00</div>
    <div class="hour-row"><span>▦ Sunday</span>h.6:00-h.24:00</div>
    <p>Lorem ipsum dolor sit amet, consectetuer adipiscing elit, sed diam nonummy nibh euismod tincidunt ut laoreet</p>
    <strong>Enjoy it!</strong>
  </div>
</section>

<section>
  <div class="abs tweet-mark"></div>
  <p class="abs tweet">aliquam erat volutpat. Ut wisi enim ad minim veniam, quis nostrud exerci tation ullamcorper suscipit lobortis nisl ut aliquip ex ea commodo consequat. Duis autem vel <span>2 days ago</span></p>
</section>

<footer>
  <div class="abs footer"></div>
  <div class="abs newsletter" style="color:#fff">
    <h3 class="f-title">Newsletter signup</h3>
    <p>Lorem ipsum dolor sit amet, consectetuer adipiscing elit sed diam nonummy.</p>
    <div class="field">INSERT EMAIL</div>
    <div class="submit"><span>SUBMIT EMAIL</span><span>›</span></div>
  </div>
  <p class="abs foot-about" style="color:#fff">Lorem ipsum dolor sit amet, consectetuer adipiscing elit, sed diam nonummy nibh euismod tincidunt ut laoreet dolore magna aliquam erat volutpat. Ut wisi enim ad minim veniam, quis</p>
  <div class="abs foot-contact" style="color:#fff">
    <div>Phone : <b>(00) 555 010 144</b></div>
    <div>Email : <b>hello@kestrelgym.example</b></div>
  </div>
  <div class="abs foot-list" style="left:822px;color:#fff">
    <h3 class="f-title">Menu</h3>
    <ul><li>About</li><li>Trainers</li><li>Classes</li><li>Pricing</li><li>Privacy</li><li>Contact</li></ul>
  </div>
  <div class="abs foot-list" style="left:983px;color:#fff">
    <h3 class="f-title">Community</h3>
    <ul><li>Blog</li><li>Forum</li><li>Support</li><li>Newsletter</li></ul>
  </div>
  <div class="abs foot-bar"><span style="position:absolute;left:93px;top:13px">© 2014 Template by Kestrel Calisthenics Gym</span></div>
  <div class="abs social-bottom"><i></i><i></i><i></i><i></i><i></i><i></i><i></i></div>
</footer>

</body>
</html>
```